Prosthetic Brochure

Looking for a trifold brochure that highlights our Prosthetic department. Has to have good stock pictures of prosthetic care. Should have Prosthetic Services from our website www.brindlemoorclinic.com I would like it in the same colors of our website.

Target Market(s)

Patients and physicians

Industry/Entity Type

Medical

Requirements
Must have
• Pictures of people helping prosthetic patients and information from the flyer I uploaded and our website under Prosthetic services.
Nice to have
• Same color scheme as our website. Blue with orange highlights
Should not have
• Just prosthetics no pictures of braces ( orthotics)

```html
<!DOCTYPE html>
<html lang="en">
<head>
<meta charset="utf-8">
<title>Brindlemoor Prosthetic Clinic – Trifold Brochure</title>
<link href="https://fonts.googleapis.com/css2?family=Poppins:wght@400;500;600;700;800&display=swap" rel="stylesheet">
<style>
:root{
  --blue:#1763c6;
  --blue-dark:#0b4aa3;
  --blue-light:#2c82e0;
  --orange:#f05a0a;
  --orange-light:#ff7d1f;
  --white:#ffffff;
  --ink:#2d2d2d;
  --rule:#c9c9c9;
  --page:#eeeeee;
}
*{box-sizing:border-box;margin:0;padding:0}
html,body{width:1200px;height:2650px;overflow:hidden}
body{background:var(--page);font-family:'Poppins',sans-serif;color:var(--ink);position:relative}
.spread{position:absolute;left:30px;width:1140px;height:806px;display:flex;box-shadow:0 8px 24px rgba(0,0,0,.25);background:var(--white)}
.spread--outside{top:500px}
.spread--inside{top:1346px}
.panel{position:relative;width:380px;height:100%;overflow:hidden}
.panel--blue{background:linear-gradient(160deg,var(--blue-light),var(--blue) 45%,var(--blue-dark))}
.panel--white{background:var(--white)}
.photo{position:absolute;border-radius:50%;border:6px solid var(--white)}

/* about */
.badge{position:absolute;left:105px;top:30px;width:145px;height:145px;border-radius:50%;background:var(--white);border:8px solid #1f3f7a}
.about-title{position:absolute;left:48px;top:184px;color:var(--white);font-size:26px;font-weight:400;letter-spacing:.5px}
.about-title b{font-weight:800}
.about-copy{position:absolute;left:48px;top:228px;width:300px;color:var(--white);font-size:10.6px;line-height:1.22}
.about-copy p+p{margin-top:12px}
.photo--about{left:0;top:505px;width:420px;height:420px;background:radial-gradient(circle at 60% 40%,#e9c9a6,#a7a39c 45%,#3f4247)}

/* brand */
.brand{position:absolute;left:0;width:100%;text-align:center;font-weight:700;color:var(--blue-dark)}
.brand .dot{display:inline-block;width:14px;height:14px;border-radius:50%;background:var(--orange);vertical-align:middle;margin-right:6px}

/* locations */
.loc-title{position:absolute;top:100px;left:0;width:100%;text-align:center;color:var(--blue);font-size:25px;font-weight:700}
.loc-list{position:absolute;left:61px;top:148px;width:258px;display:flex;flex-direction:column;gap:12px}
.loc{position:relative;border:2px solid var(--blue);border-radius:10px;overflow:visible;background:var(--white)}
.loc-pin{position:absolute;left:50%;top:-12px;transform:translateX(-50%);width:24px;height:24px;border-radius:50%;background:var(--blue);border:2px solid var(--white);display:flex;align-items:center;justify-content:center}
.loc-address{background:linear-gradient(var(--orange-light),var(--orange));color:var(--white);text-align:center;font-size:12.5px;font-weight:500;line-height:1.15;padding:14px 8px 10px;border-radius:8px 8px 0 0;height:58px;display:flex;align-items:center;justify-content:center}
.loc-phone{height:36px;display:flex;align-items:center;justify-content:center;gap:8px;color:var(--blue-dark);font-size:19px;font-weight:500}
.web{position:absolute;left:50%;transform:translateX(-50%);top:730px;display:flex;height:28px;border-radius:6px;overflow:hidden;background:var(--orange)}
.web-icon{width:36px;background:var(--blue);display:flex;align-items:center;justify-content:center}
.web-url{color:var(--white);font-size:15px;font-weight:600;padding:0 18px;display:flex;align-items:center;white-space:nowrap}

/* cover */
.panel--cover{background:linear-gradient(to bottom,var(--white) 0,var(--white) 17%,var(--blue-light) 32%,var(--blue) 60%,var(--blue-dark))}
.photo--team{left:4px;top:160px;width:372px;height:372px;background:linear-gradient(180deg,#8a5d49,#9fb0c4 45%,#4d6f9e);border-width:7px;box-shadow:0 4px 10px rgba(0,0,0,.25)}
.cover-title{position:absolute;top:568px;left:0;width:100%;text-align:center;color:var(--white);font-size:36px;font-weight:800;line-height:.98}
.cover-sub{position:absolute;top:684px;left:0;width:100%;text-align:center;color:var(--white);font-size:15px;font-weight:700;line-height:1.3}
.panel--cover .web{top:742px}

/* why */
.why-title{position:absolute;left:38px;top:34px;color:var(--white);font-size:24px;line-height:1.08;font-weight:400}
.why-title b{font-weight:800}
.why-list{position:absolute;left:38px;top:100px;width:310px;list-style:none;color:var(--white)}
.why-list li{position:relative;padding-left:22px;margin-bottom:14px}
.why-list li::before{content:"";position:absolute;left:0;top:4px;width:11px;height:11px;border-radius:50%;background:var(--orange);border:2px solid var(--white)}
.why-list h3{font-size:14.5px;font-weight:700;line-height:1.1}
.why-list p{font-size:10.5px;line-height:1.2;margin-top:2px}
.why-close{position:absolute;left:44px;top:430px;width:300px;color:var(--white);font-size:13px;line-height:1.15}
.cta{position:absolute;left:41px;top:468px;width:300px;background:var(--white);border:2px solid var(--white);border-radius:6px;overflow:hidden}
.cta-text{background:var(--orange);color:var(--white);text-align:center;font-size:13px;line-height:1.15;padding:4px 6px}
.cta-phone{color:var(--blue-dark);text-align:center;font-size:13.5px;font-weight:600;padding:3px;display:flex;justify-content:center;gap:6px;align-items:center}
.photo--hands{left:0;top:560px;width:380px;height:380px;background:radial-gradient(circle at 45% 40%,#c2a98e,#6f8a5a 45%,#3a5534)}

/* staff */
.staff-list{position:absolute;left:30px;width:320px;display:flex;flex-direction:column}
.staff{padding-bottom:10px;border-bottom:1px solid var(--rule)}
.staff:last-child{border-bottom:none}
.staff-head{position:relative;height:100px}
.staff-photo{position:absolute;left:0;top:0;width:100px;height:100px;border-radius:50%;background:linear-gradient(#cfd3d8,#8c96a3);border:3px solid var(--white);box-shadow:0 1px 4px rgba(0,0,0,.3);z-index:2}
.staff-tag{position:absolute;left:80px;right:0;top:4px;height:92px;border-radius:14px;color:var(--white);text-align:center;padding-left:20px;display:flex;flex-direction:column;justify-content:center}
.staff-tag--blue{background:var(--blue-dark)}
.staff-tag--orange{background:linear-gradient(var(--orange-light),var(--orange))}
.staff-tag h4{font-size:15px;font-weight:800;line-height:1.1;white-space:nowrap}
.staff-tag span{font-size:11.5px;line-height:1.12}
.staff-bio{font-size:9.8px;line-height:1.22;margin-top:8px}
.staff-list--left{top:26px;gap:14px}
.staff-list--right{top:34px;gap:36px}
.staff-list--right .staff{padding-bottom:26px}
</style>
</head>
<body>

<section class="spread spread--outside">
  <div class="panel panel--blue">
    <div class="badge" role="img" aria-label="Certification board seal"></div>
    <h2 class="about-title">ABOUT <b>US</b></h2>
    <div class="about-copy">
      <p>Brindlemoor Prosthetic Clinic has been providing quality, compassionate care to residents of Fernwood and the surrounding region since 1983. A recognized leader in the field, our experts work as a team to create the most functional solution to your orthotic, prosthetic and pedorthic needs using the latest technology available. Our patient-centered, team approach means we work closely with your doctor, nurse, therapist and family to create custom made solutions that work for you.</p>
      <p>Our practitioners make up the largest and most experienced O &amp; P practice in the area. We have both adult and pediatric specialists. Our board-certified practitioners regularly attend and conduct continuing education programs and clinics allowing us to bring our patients the very latest in technology and developments in the field. Our Fernwood based Central Fabrication Facility allows us to fabricate your device with speed, quality, and convenience.</p>
    </div>
    <div class="photo photo--about" role="img" aria-label="Practitioner fitting a prosthetic socket in the fabrication lab"></div>
  </div>

  <div class="panel panel--white">
    <div class="brand" style="top:48px;font-size:15px"><span class="dot"></span>Brindlemoor Prosthetic Clinic</div>
    <h2 class="loc-title">LOCATIONS</h2>
    <div class="loc-list">
      <div class="loc"><span class="loc-pin"><svg width="10" height="13" viewBox="0 0 10 13"><path d="M5 0a5 5 0 0 0-5 5c0 3.6 5 8 5 8s5-4.4 5-8a5 5 0 0 0-5-5z" fill="#fff"/><circle cx="5" cy="5" r="1.8" fill="#1763c6"/></svg></span><div class="loc-address">512 Alder Lane<br>Fernwood, MO 63100</div><div class="loc-phone"><svg width="14" height="14" viewBox="0 0 24 24"><path d="M6.6 10.8a15 15 0 0 0 6.6 6.6l2.2-2.2c.3-.3.7-.4 1-.2 1.1.4 2.3.6 3.6.6.6 0 1 .4 1 1V20c0 .6-.4 1-1 1A17 17 0 0 1 3 4c0-.6.4-1 1-1h3.5c.6 0 1 .4 1 1 0 1.3.2 2.5.6 3.6.1.3 0 .7-.2 1z" fill="#0b4aa3"/></svg>(555) 201-4410</div></div>
      <div class="loc"><span class="loc-pin"><svg width="10" height="13" viewBox="0 0 10 13"><path d="M5 0a5 5 0 0 0-5 5c0 3.6 5 8 5 8s5-4.4 5-8a5 5 0 0 0-5-5z" fill="#fff"/><circle cx="5" cy="5" r="1.8" fill="#1763c6"/></svg></span><div class="loc-address">Riverside Medical Pavilion<br>Suite 4B, Fernwood, MO 63101</div><div class="loc-phone"><svg width="14" height="14" viewBox="0 0 24 24"><path d="M6.6 10.8a15 15 0 0 0 6.6 6.6l2.2-2.2c.3-.3.7-.4 1-.2 1.1.4 2.3.6 3.6.6.6 0 1 .4 1 1V20c0 .6-.4 1-1 1A17 17 0 0 1 3 4c0-.6.4-1 1-1h3.5c.6 0 1 .4 1 1 0 1.3.2 2.5.6 3.6.1.3 0 .7-.2 1z" fill="#0b4aa3"/></svg>(555) 201-4422</div></div>
      <div class="loc"><span class="loc-pin"><svg width="10" height="13" viewBox="0 0 10 13"><path d="M5 0a5 5 0 0 0-5 5c0 3.6 5 8 5 8s5-4.4 5-8a5 5 0 0 0-5-5z" fill="#fff"/><circle cx="5" cy="5" r="1.8" fill="#1763c6"/></svg></span><div class="loc-address">88 Kestrel Road, Suite 110<br>Fernwood, MO 63102</div><div class="loc-phone"><svg width="14" height="14" viewBox="0 0 24 24"><path d="M6.6 10.8a15 15 0 0 0 6.6 6.6l2.2-2.2c.3-.3.7-.4 1-.2 1.1.4 2.3.6 3.6.6.6 0 1 .4 1 1V20c0 .6-.4 1-1 1A17 17 0 0 1 3 4c0-.6.4-1 1-1h3.5c.6 0 1 .4 1 1 0 1.3.2 2.5.6 3.6.1.3 0 .7-.2 1z" fill="#0b4aa3"/></svg>(555) 201-4433</div></div>
      <div class="loc"><span class="loc-pin"><svg width="10" height="13" viewBox="0 0 10 13"><path d="M5 0a5 5 0 0 0-5 5c0 3.6 5 8 5 8s5-4.4 5-8a5 5 0 0 0-5-5z" fill="#fff"/><circle cx="5" cy="5" r="1.8" fill="#1763c6"/></svg></span><div class="loc-address">3100 Linden Court, Ste. 120<br>Halberg, MO 63105</div><div class="loc-phone"><svg width="14" height="14" viewBox="0 0 24 24"><path d="M6.6 10.8a15 15 0 0 0 6.6 6.6l2.2-2.2c.3-.3.7-.4 1-.2 1.1.4 2.3.6 3.6.6.6 0 1 .4 1 1V20c0 .6-.4 1-1 1A17 17 0 0 1 3 4c0-.6.4-1 1-1h3.5c.6 0 1 .4 1 1 0 1.3.2 2.5.6 3.6.1.3 0 .7-.2 1z" fill="#0b4aa3"/></svg>(555) 201-4444</div></div>
      <div class="loc"><span class="loc-pin"><svg width="10" height="13" viewBox="0 0 10 13"><path d="M5 0a5 5 0 0 0-5 5c0 3.6 5 8 5 8s5-4.4 5-8a5 5 0 0 0-5-5z" fill="#fff"/><circle cx="5" cy="5" r="1.8" fill="#1763c6"/></svg></span><div class="loc-address">6 Copper Terrace, Ste. 2<br>Ashmont, IL 62200</div><div class="loc-phone"><svg width="14" height="14" viewBox="0 0 24 24"><path d="M6.6 10.8a15 15 0 0 0 6.6 6.6l2.2-2.2c.3-.3.7-.4 1-.2 1.1.4 2.3.6 3.6.6.6 0 1 .4 1 1V20c0 .6-.4 1-1 1A17 17 0 0 1 3 4c0-.6.4-1 1-1h3.5c.6 0 1 .4 1 1 0 1.3.2 2.5.6 3.6.1.3 0 .7-.2 1z" fill="#0b4aa3"/></svg>(555) 201-4455</div></div>
    </div>
    <div class="web"><span class="web-icon"><svg width="16" height="16" viewBox="0 0 16 16" fill="none" stroke="#fff" stroke-width="1.2"><circle cx="8" cy="8" r="7"/><ellipse cx="8" cy="8" rx="3" ry="7"/><path d="M1 8h14M2.5 4.5h11M2.5 11.5h11"/></svg></span><span class="web-url">www.brindlemoorclinic.com</span></div>
  </div>

  <div class="panel panel--cover">
    <div class="brand" style="top:60px;font-size:17px"><span class="dot"></span>Brindlemoor Prosthetic Clinic</div>
    <div class="photo photo--team" role="img" aria-label="Group photo of the prosthetic team outside the clinic"></div>
    <h1 class="cover-title">MEET OUR<br>PROSTHETIC<br>TEAM</h1>
    <p class="cover-sub">WE'RE MAKING A DIFFERENCE<br>IN PEOPLES LIVES...</p>
    <div class="web"><span class="web-icon"><svg width="16" height="16" viewBox="0 0 16 16" fill="none" stroke="#fff" stroke-width="1.2"><circle cx="8" cy="8" r="7"/><ellipse cx="8" cy="8" rx="3" ry="7"/><path d="M1 8h14M2.5 4.5h11M2.5 11.5h11"/></svg></span><span class="web-url">www.brindlemoorclinic.com</span></div>
  </div>
</section>

<section class="spread spread--inside">
  <div class="panel panel--blue">
    <h2 class="why-title">WHY USE <b>BRINDLEMOOR<br>PROSTHETIC CLINIC?</b></h2>
    <ul class="why-list">
      <li><h3>FIRST-CLASS PATIENT CARE</h3><p>Our facility is accredited by the national certification board. We have met rigid standards that put patient needs and safety first</p></li>
      <li><h3>HIGH-END TECHNOLOGY</h3><p>We are always current on the latest socket and component technology</p></li>
      <li><h3>EXPERIENCE</h3><p>78 years of combined technical &amp; practitioner experience</p></li>
      <li><h3>FAST TURNAROUND</h3><p>Same week check sockets, complete definitive prosthesis in 30 days ( pending insurance authorizations)</p></li>
      <li><h3>A FIRM BELIEF IN TEAMWORK</h3><p>We love to work with the patient, rehabilitative staff and physicians to achieve the patient's goals.</p></li>
    </ul>
    <p class="why-close">All of these combined allow us to provide the best possible patient outcome</p>
    <div class="cta">
      <div class="cta-text">Call us today for a free consult and prosthetic check-up</div>
      <div class="cta-phone"><svg width="12" height="12" viewBox="0 0 24 24"><path d="M6.6 10.8a15 15 0 0 0 6.6 6.6l2.2-2.2c.3-.3.7-.4 1-.2 1.1.4 2.3.6 3.6.6.6 0 1 .4 1 1V20c0 .6-.4 1-1 1A17 17 0 0 1 3 4c0-.6.4-1 1-1h3.5c.6 0 1 .4 1 1 0 1.3.2 2.5.6 3.6.1.3 0 .7-.2 1z" fill="#f05a0a"/></svg>(555) 201-4410</div>
    </div>
    <div class="photo photo--hands" role="img" aria-label="Prosthetic hand reaching toward a human hand outdoors"></div>
  </div>

  <div class="panel panel--white">
    <div class="staff-list staff-list--left">
      <article class="staff">
        <div class="staff-head"><div class="staff-photo" role="img" aria-label="Portrait of Daniel Forde"></div><div class="staff-tag staff-tag--blue"><h4>DANIEL FORDE, CPO</h4><span>NATIONAL BOARD CERTIFIED<br>PROSTHETIST &amp; ORTHOTIST</span></div></div>
        <p class="staff-bio">Daniel has dual Master's Degrees in Prosthetics and Orthotics and in Business Administration. His undergrad was in Athletic training. Daniel is up to date on the latest cutting edge prosthetic technology and loves the advancements being made in prosthetics</p>
      </article>
      <article class="staff">
        <div class="staff-head"><div class="staff-photo" role="img" aria-label="Portrait of Rachel Lindqvist"></div><div class="staff-tag staff-tag--orange"><h4>RACHEL LINDQVIST, CPO</h4><span>NATIONAL BOARD CERTIFIED<br>PROSTHETIST &amp; ORTHOTIST</span></div></div>
        <p class="staff-bio">Rachel graduated from Gulf State University with her Master of Science in Prosthetics and Orthotics. She has been practicing Prosthetics and Orthotics since 2018. Rachel is a people person and loves working with patients</p>
      </article>
      <article class="staff">
        <div class="staff-head"><div class="staff-photo" role="img" aria-label="Portrait of Marco Ellison"></div><div class="staff-tag staff-tag--blue"><h4>MARCO ELLISON, CPO</h4><span>NATIONAL BOARD CERTIFIED<br>CLINICAL FELLOW</span></div></div>
        <p class="staff-bio">Marco grew up in Fernwood and went to Fernwood College where he graduated in biomedical engineering. He graduated from Southfield Medical School with a Masters Degree in Prosthetics and Orthotics. His hobbies include playing soccer and he is passionate about helping others.</p>
      </article>
      <article class="staff">
        <div class="staff-head"><div class="staff-photo" role="img" aria-label="Portrait of Peter Haskins"></div><div class="staff-tag staff-tag--orange"><h4>PETER HASKINS, CO</h4><span>NATIONAL BOARD-CERTIFIED<br>ORTHOTIST<br>AND RESIDENT PROSTHETIST</span></div></div>
        <p class="staff-bio">Peter graduated with a Masters in Prosthetic &amp; Orthotics from Lakeshore University. He is a former High School teacher and coach (football, wrestling and rugby). Peter loves working with children with disabilities and helping them regain lost function. He loves working with his hands to make devices that help other achieve their functional goals.</p>
      </article>
    </div>
  </div>

  <div class="panel panel--white">
    <div class="staff-list staff-list--right">
      <article class="staff">
        <div class="staff-head"><div class="staff-photo" role="img" aria-label="Portrait of Harold Whitcombe"></div><div class="staff-tag staff-tag--orange"><h4>HAROLD WHITCOMBE, CPO</h4><span>NATIONAL BOARD CERTIFIED<br>PROSTHETIST &amp; ORTHOTIST</span></div></div>
        <p class="staff-bio">With over 46 years of prosthetic experience, Harold has been a leader and past president of our National organization and is highly respected for his experience and knowledge.</p>
      </article>
      <article class="staff">
        <div class="staff-head"><div class="staff-photo" role="img" aria-label="Portrait of Clara Benning"></div><div class="staff-tag staff-tag--blue"><h4>CLARA BENNING, CPO</h4><span>NATIONAL BOARD CERTIFIED<br>PROSTHETIST &amp; ORTHOTIST</span></div></div>
        <p class="staff-bio">Clara graduated from Lakeshore University with her Masters Degree in Prosthetics &amp; Orthotics. Clara did her undergrad at Fernwood College in biomedical Engineering. Clara is a Fernwood native and loves this city.</p>
      </article>
      <article class="staff">
        <div class="staff-head"><div class="staff-photo" role="img" aria-label="Portrait of Owen Marlett"></div><div class="staff-tag staff-tag--orange"><h4>OWEN MARLETT, CPO</h4><span>NATIONAL BOARD CERTIFIED<br>ORTHOTIST &amp; RESIDENT<br>PROSTHETIST</span></div></div>
        <p class="staff-bio">Owen graduated from Three Rivers University with a Master Degree in Prosthetics and Orthotics. His undergrad is in exercise physiology from Ozark State. Owen is a huge outdoor enthusiast and loves helping people regain their independence</p>
      </article>
    </div>
    <div class="web"><span class="web-icon"><svg width="16" height="16" viewBox="0 0 16 16" fill="none" stroke="#fff" stroke-width="1.2"><circle cx="8" cy="8" r="7"/><ellipse cx="8" cy="8" rx="3" ry="7"/><path d="M1 8h14M2.5 4.5h11M2.5 11.5h11"/></svg></span><span class="web-url">www.brindlemoorclinic.com</span></div>
  </div>
</section>

</body>
</html>
```